Tourist Park Brochures

www.brightmoor.com.au

I am looking to create a brochure (fold out) for each of the 7 Brightmoor Properties and a new ‘group’ Brochure. I am looking for a fresh theme, with the following components:
· Brightmoor Logo (top Left)
· Wide Camps Logo (Top Right)
· Location Band immediately beneath the two logos
· Contact details bottom of brochure
· Map on Back of Brochure

I would like to keep the brochures friendly and family orientated with clear information.

I would like to start with Kindlow Meadows Caravan Park and once chosen the design negotiate to do the remaining properties.
Updates

Project Deadline Extended
Reason: Previous round did not fit brief, trying again

Target Market(s)

Older travellers, young families, couples

Industry/Entity Type

Group

Font styles to use
Serif

Colors
85cae6
3377b5
0293ce
cedeed
cfe9f5
89d0c7
86cfc6

Requirements
Must have
• Be a fold out DL sized brochure
• · Brightmoor Logo (top Left)
• · Wide Camps Logo (Top Right)
• · Location Band immediately beneath the two logos
• · Contact details
• · Map on Back of Brochure
• Map of where other Brightmoor Properties are with Brightmoor website

```html
<!DOCTYPE html>
<html lang="en">
<head>
<meta charset="utf-8">
<title>Kindlow Meadows Caravan Park – Brochure</title>
<link href="https://fonts.googleapis.com/css2?family=Lato:wght@400;700&family=Libre+Baskerville:wght@400;700&family=Oswald:wght@600&display=swap" rel="stylesheet">
<style>
  :root{
    --stage:#6b8bae;
    --blue:#0293ce;
    --blue-deep:#3377b5;
    --navy:#1b4f86;
    --teal:#86cfc6;
    --sky:#cfe9f5;
    --mist:#cedeed;
    --paper:#f4f5f6;
    --ink:#2f3a44;
    --white:#ffffff;
  }
  *{box-sizing:border-box;margin:0;padding:0}
  html,body{width:1200px;height:1200px;overflow:hidden}
  body{background:var(--stage);font-family:"Lato",sans-serif;position:relative}
  .brochure{position:absolute;left:105px;top:250px;width:990px;height:700px;display:flex;box-shadow:0 20px 40px rgba(20,40,70,.35)}
  .panel{position:relative;width:330px;height:700px;overflow:hidden}
  .panel svg.bg{position:absolute;inset:0;width:330px;height:700px}
  .abs{position:absolute}

  /* left panel */
  .about{left:26px;top:330px;width:280px;color:var(--white)}
  .about h2{font-size:17px;font-weight:700;margin-bottom:8px}
  .about p{font-size:10.5px;line-height:1.45;margin-bottom:8px}
  .about h3{font-size:17px;font-weight:700;margin:20px 0 8px;text-transform:uppercase}
  .call{left:0;width:330px;top:625px;text-align:center;color:var(--white);font-family:"Libre Baskerville",serif}
  .call .line1{font-size:15px;letter-spacing:.5px}
  .call .line2{font-size:12px;margin-top:2px}

  /* brand name */
  .brand{font-family:"Lato",sans-serif;font-weight:700;font-size:18px;color:var(--ink);line-height:1}

  /* middle panel */
  .mid-brand{left:0;width:330px;top:208px;text-align:center}
  .map-ring{left:90px;top:245px;width:150px;height:150px;border-radius:50%;border:3px solid var(--teal);background:var(--white);padding:5px;box-shadow:0 6px 10px rgba(0,0,0,.12)}
  .map-ring .map{width:100%;height:100%;border-radius:50%;background:radial-gradient(circle at 65% 40%,#e9ecef 0 38%,#b9dcf5 39% 100%)}
  .contact{left:0;width:330px;top:430px;text-align:center;color:var(--ink)}
  .contact h2{font-family:"Libre Baskerville",serif;font-size:24px;font-weight:700;color:var(--blue);letter-spacing:.5px;margin-bottom:16px}
  .contact .row{display:flex;flex-direction:column;align-items:center;margin-bottom:12px;font-size:12.5px}
  .contact .row svg{width:18px;height:18px;margin-bottom:4px}
  .contact .phone{font-size:16px;font-weight:700}

  /* right panel */
  .right-brand{left:28px;top:34px}
  .badge{right:26px;top:22px;width:34px;height:30px;background:#f5b81c;border-radius:6px}
  .tagline{right:28px;top:520px;text-align:right;color:var(--white)}
  .tagline .t1{font-size:29px;line-height:1.15}
  .tagline .t2{font-family:"Oswald",sans-serif;font-weight:600;font-size:56px;line-height:1;color:var(--navy);letter-spacing:1px}
  .url{right:28px;top:650px;color:var(--white);font-size:11px;letter-spacing:3.5px}
</style>
</head>
<body>
<main class="brochure">

  <section class="panel panel-inside-left">
    <svg class="bg" viewBox="0 0 330 700">
      <rect width="330" height="700" fill="var(--blue)"/>
      <path d="M0 300 C120 290 260 230 330 110 L330 0 L0 0Z" fill="var(--white)"/>
      <path d="M0 285 C120 275 250 215 322 100 L330 0 L0 0Z" fill="var(--teal)"/>
      <defs><linearGradient id="coast" x1="0" y1="0" x2="0" y2="1">
        <stop offset="0" stop-color="#3f8fe0"/><stop offset=".45" stop-color="#7fc4ef"/><stop offset=".7" stop-color="#6e9a4a"/><stop offset="1" stop-color="#a9c48a"/></linearGradient></defs>
      <path d="M0 268 C120 258 240 200 312 90 L330 60 L330 0 L0 0Z" fill="url(#coast)" role="img" aria-label="Photo of a red and white lighthouse above coastal scrub with two walkers"/>
    </svg>
    <div class="abs about">
      <h2>Kindlow Meadows Caravan Park :</h2>
      <p>Kindlow Meadows Caravan Park is a 6-minute drive from both Coralby Water Park and Gull Rock Lookout. It is an 8-minute drive from Coralby Golf Course and a 15-minute drive from Coralby Airport. All air-conditioned rooms offer indoor and outdoor dining areas. Some rooms have a spa bath, sea views, a terrace or cooking facilities.</p>
      <p>Guests can share a meal using the BBQ facilities, or enjoy the games room. This property is also rated for the best value in Coralby! Guests are getting more for their money when compared to other properties in this city.</p>
      <h3>One Night Bookings :</h3>
      <p>One night bookings are available. They must be booked direct and can only be made by phoning our office to book. A one night booking surcharge will apply.</p>
    </div>
    <div class="abs call">
      <div class="line1">CALL US (08) 9430 2718</div>
      <div class="line2">(8pm to 6pm, monday to sunday)</div>
    </div>
  </section>

  <section class="panel panel-contact">
    <svg class="bg" viewBox="0 0 330 700">
      <defs>
        <linearGradient id="paper" x1="0" y1="0" x2="0" y2="1"><stop offset="0" stop-color="#fafafa"/><stop offset="1" stop-color="#eceef0"/></linearGradient>
        <radialGradient id="family" cx=".5" cy=".5" r=".55"><stop offset="0" stop-color="#e9d6c9"/><stop offset=".6" stop-color="#f3ece6"/><stop offset="1" stop-color="#fafafa" stop-opacity="0"/></radialGradient>
      </defs>
      <rect width="330" height="700" fill="url(#paper)"/>
      <rect x="40" y="10" width="250" height="185" fill="url(#family)" role="img" aria-label="Photo of a smiling family of three on the beach"/>
    </svg>
    <div class="abs brand mid-brand">Brightmoor</div>
    <div class="abs map-ring"><div class="map" role="img" aria-label="Street map of the park location on the Coralby coast"></div></div>
    <div class="abs contact">
      <h2>CONTACT US</h2>
      <div class="row">
        <svg viewBox="0 0 24 24" fill="none" stroke="var(--blue-deep)" stroke-width="2"><path d="M12 22s7-7 7-12a7 7 0 0 0-14 0c0 5 7 12 7 12z"/><circle cx="12" cy="10" r="2.5"/></svg>
        218 Harbour Parade, Coralby, WA 6599
      </div>
      <div class="row">
        <svg viewBox="0 0 24 24" fill="var(--blue-deep)"><path d="M2 6h20v12H2z"/><path d="M2 6l10 7 10-7" stroke="#fff" stroke-width="1.5" fill="none"/></svg>
        bookings@kindlowmeadowspark.com.au
      </div>
      <div class="row phone">
        <svg viewBox="0 0 24 24" fill="none" stroke="var(--blue-deep)" stroke-width="2"><circle cx="12" cy="12" r="10"/><path d="M9 7l2 3-1.5 1.5a7 7 0 0 0 3 3L14 13l3 2-1 2c-4 0-8-4-8-8z" fill="var(--blue-deep)" stroke="none"/></svg>
        (08) 9430 2718
      </div>
    </div>
  </section>

  <section class="panel panel-cover">
    <svg class="bg" viewBox="0 0 330 700">
      <defs><linearGradient id="sunset" x1="0" y1="0" x2="1" y2="1">
        <stop offset="0" stop-color="#f7d9b0"/><stop offset=".4" stop-color="#f0a24a"/><stop offset=".75" stop-color="#b8643a"/><stop offset="1" stop-color="#7a4a33"/></linearGradient></defs>
      <rect width="330" height="700" fill="var(--blue)"/>
      <path d="M0 250 C80 330 200 350 330 345 L330 0 L0 0Z" fill="var(--white)"/>
      <path d="M0 238 C80 318 200 334 330 322 L330 0 L0 0Z" fill="var(--teal)"/>
      <path d="M0 225 C80 300 200 318 330 306 L330 0 L0 0Z" fill="#fdf7ef"/>
      <path d="M0 225 C80 300 200 318 330 306 L330 95 L0 95Z" fill="url(#sunset)" role="img" aria-label="Photo of a couple running hand in hand along the beach at sunset"/>
    </svg>
    <div class="abs brand right-brand">Brightmoor</div>
    <div class="abs badge" role="img" aria-label="Wide Camps listing badge"></div>
    <div class="abs tagline">
      <div class="t1">The Vacation<br>of your</div>
      <div class="t2">DREAMS</div>
    </div>
    <div class="abs url">www.brightmoor.com.au</div>
  </section>

</main>
</body>
</html>
```